Redesign website for small print company

Vindabrot is a small printing company in Iceland mainly servicing Students, schools, etc. We are also doing all kind of other jobs, like business cards, book printing, brochure printing etc. We are also selling books online.
Our website is: www.vindabrot.is
What we are looking for is:
- Web Design (Uncoded - PSD layout only)
- Mobile friendly design, using our current color scheme: Red, green, yellow and light gray.
- Clean simple design
- Simple, light and easy to use.
- More menu Items/drop down
Industry/Entity Type
Digital Printing
Number of Pages Required
5+ page
Requirements
Must have
- Easy navigation
- Designed for mobile
- Current color scheme (see logo)
Nice to have
- Icon based products

```html
<!DOCTYPE html>
<html lang="en">
<head>
<meta charset="utf-8">
<title>Vindabrot – Printing</title>
<link href="https://fonts.googleapis.com/css2?family=Raleway:wght@400;500;600;700&family=Open+Sans:wght@400;600&display=swap" rel="stylesheet">
<style>
:root{
  --orange:#f47a1f;
  --orange-deep:#f25a1e;
  --yellow:#f9b81b;
  --red:#e8403a;
  --green:#0e6b3a;
  --ink:#2b2b2b;
  --muted:#6f6f6f;
  --line:#dcdcdc;
  --card:#ffffff;
  --dark:#1d1d1d;
  --white:#ffffff;
}
*{margin:0;padding:0;box-sizing:border-box}
html,body{width:1200px;height:3035px;overflow:hidden}
body{position:relative;font-family:"Open Sans",sans-serif;color:var(--ink);background:var(--white)}
.abs{position:absolute}
.head{font-family:"Raleway",sans-serif}

/* hero */
.hero{left:0;top:0;width:1200px;height:600px;background:linear-gradient(90deg,var(--yellow) 0%,var(--orange) 45%,var(--orange-deep) 75%,var(--orange) 100%)}
.brand{left:78px;top:20px;display:flex;align-items:center;gap:10px;color:var(--white);font-family:"Raleway",sans-serif;font-weight:700;font-size:24px;letter-spacing:.5px}
.brand-box{width:30px;height:30px;background:var(--white)}
.nav{right:100px;top:32px;display:flex;gap:28px;font-family:"Raleway",sans-serif;font-size:13px;font-weight:500;color:var(--white);letter-spacing:.5px}
.nav span.active{border-top:2px solid var(--white);padding-top:4px;margin-top:-6px}
.nav-tools{right:70px;top:28px;display:flex;gap:36px}
.watermark{left:70px;top:190px;font-family:"Raleway",sans-serif;font-weight:700;font-size:130px;color:rgba(0,0,0,.08);letter-spacing:6px}
.bird{left:620px;top:20px;width:500px;height:535px;border-radius:40% 40% 20% 20%;background:radial-gradient(ellipse at 50% 45%,#c4111a 0%,#9e0c12 45%,rgba(160,20,20,0) 72%)}
.hero-title{left:80px;top:215px;color:var(--white);font-family:"Raleway",sans-serif;font-weight:600;font-size:48px;line-height:58px}
.btn-white{left:80px;top:365px;width:208px;height:52px;background:var(--white);color:var(--red);font-family:"Raleway",sans-serif;font-weight:600;font-size:19px;display:flex;align-items:center;justify-content:center}
.arrow{top:290px}

/* about */
.section-title{width:1200px;left:0;text-align:center;font-family:"Raleway",sans-serif;font-weight:600;font-size:40px}
.about-text{left:78px;top:735px;width:525px;font-size:12.5px;line-height:24px;color:var(--muted)}
.about-text p{margin-bottom:10px}
.btn-red{background:var(--red);color:var(--white);font-family:"Raleway",sans-serif;font-weight:600;font-size:18px;display:flex;align-items:center;justify-content:center;gap:12px}
.about-card{left:663px;top:730px;width:457px;height:250px;background:#f1f1f1;border-radius:8px;box-shadow:0 20px 30px rgba(0,0,0,.18);display:flex;align-items:center;justify-content:center;font-family:"Raleway",sans-serif;font-weight:700;font-size:38px;color:var(--ink)}
.about-card .ghost{position:absolute;left:150px;top:25px;width:160px;height:200px;background:rgba(0,0,0,.06)}
.service{top:1028px;width:322px;height:230px;background:var(--card);box-shadow:0 8px 28px rgba(0,0,0,.1);display:flex;flex-direction:column;align-items:center;justify-content:center;gap:20px;font-family:"Raleway",sans-serif;font-weight:500;font-size:19px;color:#3a3a3a}

/* products */
.products{left:0;top:1355px;width:1200px;height:605px;background:linear-gradient(120deg,#3a3a3a 0%,#1c1c1c 40%,#2a2d33 70%,#3c3f46 100%)}
.product{width:340px;text-align:center;color:var(--white)}
.product h3{font-family:"Raleway",sans-serif;font-weight:600;font-size:23px;margin:12px 0 10px}
.product p{font-size:12px;line-height:24px;color:#e4e4e4}

/* contact */
.people{left:45px;top:2040px;width:495px;height:360px;background:linear-gradient(90deg,#d8cde6,#efe6da 50%,#e8c9c6);border-radius:6px}
.contact-intro{left:603px;top:2075px;width:520px;font-size:13px;line-height:26px;color:var(--muted)}
.field{width:232px;height:36px;border-bottom:1px solid var(--line);font-size:12px;color:#888;padding-top:6px}

/* footer */
.map{left:0;top:2400px;width:600px;height:575px;background:linear-gradient(135deg,#e9ece8,#dfe3e6 60%,#e8e4d6)}
.info{left:600px;top:2400px;width:600px;height:575px;background:linear-gradient(135deg,var(--orange-deep) 0%,var(--orange) 55%,var(--yellow) 100%);color:var(--white)}
.info h4{position:absolute;left:55px;font-family:"Raleway",sans-serif;font-weight:500;font-size:21px;padding-bottom:12px;border-bottom:1px solid rgba(255,255,255,.7);width:154px}
.info .row{position:absolute;left:55px;font-size:14px;line-height:26px;display:flex;gap:14px;align-items:flex-start}
.social{position:absolute;left:55px;top:1045px}
.bottom{left:0;top:2975px;width:1200px;height:60px;background:#0c0c0c;color:#d8d8d8;font-size:13px;display:flex;align-items:center;justify-content:center;letter-spacing:.3px}
</style>
</head>
<body>

<!-- Hero -->
<section class="abs hero"></section>
<div class="abs watermark">VINDABROT</div>
<div class="abs bird" role="img" aria-label="Illustration of a red bird with green beak and feet standing"></div>
<div class="abs brand"><span class="brand-box"></span>VINDABROT</div>
<nav class="abs nav" style="right:150px"><span class="active">HOME</span><span>SERVICES</span><span>JOB SUBMIT</span><span>ABOUT US</span><span>CONTACT US</span></nav>
<div class="abs nav-tools">
  <svg width="22" height="22" viewBox="0 0 22 22" fill="none" stroke="#fff" stroke-width="2"><circle cx="9" cy="9" r="7"/><line x1="14" y1="14" x2="20" y2="20"/></svg>
  <svg width="20" height="22" viewBox="0 0 20 22" fill="none" stroke="#fff" stroke-width="2"><rect x="2" y="7" width="16" height="13"/><path d="M6 7V4a4 4 0 0 1 8 0v3"/></svg>
</div>
<h1 class="abs hero-title">Do not worry ...<br>we'll manage Þetta</h1>
<div class="abs btn-white">KNOW MORE</div>
<svg class="abs arrow" style="left:22px" width="20" height="30" viewBox="0 0 20 30" fill="none" stroke="#fff" stroke-width="4"><polyline points="15,3 4,15 15,27"/></svg>
<svg class="abs arrow" style="left:1158px" width="20" height="30" viewBox="0 0 20 30" fill="none" stroke="#fff" stroke-width="4"><polyline points="5,3 16,15 5,27"/></svg>

<!-- About -->
<h2 class="abs section-title head" style="top:652px">About us</h2>
<div class="abs about-text">
  <p>Vindabrot er fyrirtæki staðsett á háskólasvæðinu sem hefur sérhæft sig í að þjónusta skólafólk, ásamt því að sinna allri almennri prentun fyrir almenning.</p>
  <p>Vindabrot gefur út greinasöfn og frumsamdar kennslubækur fyrir námskeið, prentar lokaritgerðir fyrir nema, auk þess að vinna við ótalinn fjölda smærri verka fyrir nemendur, kennara og stofnanir. Má þar nefna bæklinga, skýrslur, spurningalista, nafnspjöld, bækur, OCR skönnun og fleira.</p>
</div>
<div class="abs btn-red" style="left:78px;top:912px;width:188px;height:48px;font-size:17px">KNOW MORE</div>
<div class="abs about-card"><span class="ghost"></span><span style="position:relative">VINDABROT</span></div>

<div class="abs service" style="left:78px">
  <svg width="86" height="70" viewBox="0 0 86 70" fill="none" stroke="var(--green)" stroke-width="4"><rect x="4" y="16" width="78" height="50" rx="4"/><path d="M30 16V6h26v10"/><line x1="4" y1="38" x2="82" y2="38"/><rect x="38" y="33" width="10" height="10"/></svg>
  SENDA VERK</div>
<div class="abs service" style="left:438px">
  <svg width="80" height="76" viewBox="0 0 80 76" fill="none" stroke="var(--green)" stroke-width="4"><path d="M40 4C18 4 4 20 4 38s16 34 34 34c8 0 8-8 4-12s-2-10 6-10h10c12 0 18-8 18-18C76 16 60 4 40 4z"/><circle cx="22" cy="32" r="5"/><circle cx="34" cy="18" r="5"/><circle cx="52" cy="20" r="5"/><circle cx="24" cy="50" r="5"/></svg>
  HANNA VERK</div>
<div class="abs service" style="left:800px">
  <svg width="50" height="80" viewBox="0 0 50 80" fill="none" stroke="var(--green)" stroke-width="5"><path d="M6 20a19 19 0 1 1 26 17c-5 2-7 6-7 11v8"/><circle cx="25" cy="70" r="3" fill="var(--green)"/></svg>
  FA TILBOD</div>

<!-- Products -->
<section class="abs products" role="img" aria-label="Dark photo of a printing press in operation"></section>
<h2 class="abs section-title head" style="top:1402px;color:var(--white)">Product List</h2>

<div class="abs product" style="left:70px;top:1480px">
  <svg width="50" height="62" viewBox="0 0 50 62" fill="none" stroke="#fff" stroke-width="3"><path d="M4 4h30l12 12v42H4z"/><line x1="12" y1="22" x2="38" y2="22"/><line x1="12" y1="32" x2="38" y2="32"/><line x1="12" y1="42" x2="38" y2="42"/></svg>
  <h3>Essays</h3><p>Vindabrot prentar út og bindur inn ritgerðir. Ritgerðir eru ýmist kiljuinnbundnar...</p></div>
<div class="abs product" style="left:430px;top:1480px">
  <svg width="74" height="62" viewBox="0 0 74 62" fill="none" stroke="#fff" stroke-width="3"><rect x="4" y="10" width="66" height="46"/><rect x="14" y="20" width="18" height="20"/><line x1="40" y1="24" x2="62" y2="24"/><line x1="40" y1="34" x2="62" y2="34"/><line x1="14" y1="48" x2="62" y2="48"/></svg>
  <h3>Business cards</h3><p>Nafnspjöld hjá Vindabroti er hægt að prenta í öllum stærðum og gerðum, en algengast...</p></div>
<div class="abs product" style="left:790px;top:1480px">
  <svg width="66" height="62" viewBox="0 0 66 62" fill="none" stroke="#fff" stroke-width="3"><path d="M4 8l19-4 20 4 19-4v50l-19 4-20-4-19 4z"/><line x1="23" y1="4" x2="23" y2="54"/><line x1="43" y1="8" x2="43" y2="58"/></svg>
  <h3>Leafleats</h3><p>Vindabrot prentar bæklinga í öllum stærðum og gerðum og á ýmsar tegundir pappírs.</p></div>

<div class="abs product" style="left:70px;top:1710px">
  <svg width="52" height="64" viewBox="0 0 52 64" fill="none" stroke="#fff" stroke-width="3"><rect x="4" y="4" width="44" height="56"/><line x1="12" y1="4" x2="12" y2="60"/><line x1="20" y1="20" x2="40" y2="20"/></svg>
  <h3>Bookprinting</h3><p>Vindabrot sérhæfir sig í að prenta bækur í litlu upplagi, við höfum frábæran búnað til...</p></div>
<div class="abs product" style="left:430px;top:1710px">
  <svg width="50" height="64" viewBox="0 0 50 64" fill="none" stroke="#fff" stroke-width="3"><rect x="8" y="8" width="34" height="50"/><path d="M4 8h42M4 58h42"/><circle cx="25" cy="4" r="2"/></svg>
  <h3>Posters</h3><p>Vindabrot prentar veggspjöld í öllum stærðum fyrir ráðstefnur, sýningar og kynningar...</p></div>
<div class="abs product" style="left:790px;top:1710px">
  <svg width="60" height="64" viewBox="0 0 60 64" fill="none" stroke="#fff" stroke-width="3"><rect x="4" y="8" width="50" height="12" rx="3"/><rect x="8" y="24" width="48" height="12" rx="3"/><rect x="4" y="40" width="50" height="12" rx="3"/><line x1="12" y1="58" x2="50" y2="58"/></svg>
  <h3>Textbooks</h3><p>Vindabrot prentar út og bindur inn kennslubækur. Bækur eru ýmist kiljuinnbundnar...</p></div>

<!-- Contact -->
<h2 class="abs section-title head" style="top:1985px">Contact us</h2>
<div class="abs people" role="img" aria-label="Photo of three smiling students holding books"></div>
<p class="abs contact-intro">Lorem Ipsum is simply dummy text of the printing and typesetting industry. Lorem Ipsum has been the industry.</p>
<div class="abs field" style="left:603px;top:2150px">Name</div>
<div class="abs field" style="left:890px;top:2150px">Email</div>
<div class="abs field" style="left:603px;top:2215px">Phone</div>
<div class="abs field" style="left:890px;top:2215px">Subject</div>
<div class="abs btn-red" style="left:603px;top:2288px;width:208px;height:46px">SEND NOW
  <svg width="24" height="22" viewBox="0 0 24 22" fill="#fff"><path d="M1 10L23 1 18 21 11 14 19 5 8 12z"/></svg></div>

<!-- Footer -->
<div class="abs map" role="img" aria-label="Street map showing the shop location"></div>
<div class="abs info">
  <h4 style="top:70px">CONTACT US</h4>
  <div class="row" style="top:128px;width:340px">
    <svg width="14" height="20" viewBox="0 0 14 20" fill="#fff" style="margin-top:4px"><path d="M7 0a7 7 0 0 1 7 7c0 5-7 13-7 13S0 12 0 7a7 7 0 0 1 7-7z"/><circle cx="7" cy="7" r="2.5" fill="var(--orange)"/></svg>
    <span>Lorem Ipsum is simply dummy text of the printing.</span></div>
  <div class="row" style="top:192px;gap:60px">
    <span style="display:flex;gap:14px;align-items:center"><svg width="15" height="15" viewBox="0 0 24 24" fill="#fff"><path d="M6.6 10.8a15 15 0 0 0 6.6 6.6l2.2-2.2c.3-.3.7-.4 1-.2 1.1.4 2.3.6 3.6.6.6 0 1 .4 1 1V20c0 .6-.4 1-1 1A17 17 0 0 1 3 4c0-.6.4-1 1-1h3.5c.6 0 1 .4 1 1 0 1.3.2 2.5.6 3.6.1.3 0 .7-.2 1z"/></svg>555 0142</span>
    <span style="display:flex;gap:14px;align-items:center"><svg width="18" height="14" viewBox="0 0 18 14" fill="none" stroke="#fff" stroke-width="1.6"><rect x="1" y="1" width="16" height="12"/><polyline points="1,1 9,8 17,1"/></svg>verk@vindabrot.is</span></div>
  <h4 style="top:255px;width:154px">OPENING HOURS</h4>
  <div class="row" style="top:326px;gap:70px"><span>Mon - Fri : 09:00-17:00</span><span>Weekends: Closed</span></div>
  <h4 style="top:380px;width:170px">FOLLOW US ON</h4>
  <svg style="position:absolute;left:55px;top:452px" width="42" height="42" viewBox="0 0 42 42" fill="none" stroke="#fff" stroke-width="1.5"><circle cx="21" cy="21" r="19"/></svg>
</div>
<div class="abs bottom">©VINDABROT - 2018. All Rights Reserved.</div>

</body>
</html>
```